DESIGN FOR TRADE SHOW FLOOR DISPLAY

March 25: I FORGOT TO INCLUDE THE OUTLINE OF WHAT I WANT FOR THE BOOTH. I JUST ADDED IT HERE. The document is called BOOTH DESIGN.

I need a design for a booth for trade shows. To see what I mean, please look at image 1 attached below.

The back wall part of the display shows graphics on the front of the display as well as the sides of the display.

I also need to have a design for the podium. See image 1 below.

I've attached the specifications for the designs.

The document for the back wall is called GRAPHIC TEMPLATE DESIGN FOR BACK WALL.

The document for the podium is called PODIUM TEMPLATE.

I've attached two other documents:

1. A large image of the cover of my book.

2. A copy of the Wrenfield Capital logo.

I think this is everything that you will need. Please let me know if there is anything else that you need.

Thanks!

Ned Calloway

Target Market(s)

CPAs and accountants. Financial professionals.

Industry/Entity Type

Trade

Font styles to use
Other font styles liked:
• Use your best idea to worth with book cover and logo.

Requirements
Must have
• The colors and fonts work well with both the book cover and the Wrenfield Capital logo.
• I've attached samples of booth designs that I like. They are called Sample 1, Sample 2, Sample 3, Sample 4. They are in no particular order.

```html
<!DOCTYPE html>
<html lang="en">
<head>
<meta charset="utf-8">
<title>Strategic Alliance Program – Booth Graphics</title>
<link rel="stylesheet" href="https://fonts.googleapis.com/css2?family=Marcellus+SC&family=Marcellus&family=Oswald:wght@500&family=Cinzel:wght@500&display=swap">
<style>
  :root {
    --bg: #e9e9e9;
    --sky: #a6e6fb;
    --sky-light: #d7f4fd;
    --navy: #0b4f86;
    --band: #0d5a94;
    --ink: #0b1f33;
    --bullet: #0d5a94;
    --water: #9fd8f2;
    --white: #ffffff;
    --cover-dark: #0a1526;
    --cover-blue: #2a86c9;
    --title-white: #ffffff;
    --title-blue: #5cc3f2;
    --brand-green: #3aa845;
  }
  * { margin: 0; padding: 0; box-sizing: border-box; }
  html, body { width: 1200px; height: 1000px; overflow: hidden; background: var(--bg); }
  body { position: relative; font-family: "Marcellus", serif; }

  .back-wall {
    position: absolute; left: 60px; top: 50px; width: 1080px; height: 620px;
    background: linear-gradient(to bottom, var(--white) 55%, var(--sky-light) 72%, var(--water) 100%);
    overflow: hidden;
  }
  .back-wall .side-band { position: absolute; top: 0; bottom: 0; width: 30px; background: var(--band); z-index: 3; }
  .back-wall .side-band.left { left: 0; }
  .back-wall .side-band.right { right: 0; }
  .back-wall .swoosh { position: absolute; left: 0; top: 0; width: 1080px; height: 300px; }

  .wall-heading {
    position: absolute; top: 62px; left: 0; right: 0; text-align: center;
    font-family: "Marcellus SC", serif; font-weight: 400; font-size: 44px; color: var(--ink); letter-spacing: 0.5px; z-index: 2;
  }

  .book {
    position: absolute; background: var(--cover-dark); overflow: hidden;
    box-shadow: 6px 6px 14px rgba(0,0,0,0.35);
  }
  .book .portrait {
    position: absolute; left: 0; top: 0; width: 62%; height: 78%;
    background: linear-gradient(135deg, #5a5f66 0%, #2b2f36 60%, #141a24 100%);
  }
  .book .cover-glow {
    position: absolute; right: 0; top: 0; width: 45%; height: 78%;
    background: linear-gradient(to bottom, #103a6a, var(--cover-blue));
  }
  .book .title {
    position: absolute; right: 6%; text-align: right;
    font-family: "Oswald", sans-serif; font-weight: 500; line-height: 0.98; text-transform: uppercase;
  }
  .book .title .w { color: var(--title-white); display: block; }
  .book .title .b { color: var(--title-blue); display: block; }
  .book .subtitle {
    position: absolute; left: 0; right: 0; background: var(--cover-blue); color: var(--white);
    font-family: "Marcellus SC", serif;
    text-align: center; line-height: 1.05; border-top: 2px solid var(--white); border-bottom: 2px solid var(--white);
  }
  .book .author {
    position: absolute; left: 0; right: 0; text-align: center; color: var(--white);
    font-family: "Cinzel", serif; letter-spacing: 4px;
  }

  .wall-book { left: 130px; top: 195px; width: 240px; height: 410px; z-index: 2; }
  .wall-book .title { top: 62px; font-size: 46px; }
  .wall-book .subtitle { top: 322px; padding: 5px 4px; font-size: 15px; }
  .wall-book .author { top: 372px; font-size: 16px; }

  .benefits {
    position: absolute; left: 430px; top: 325px; list-style: none; z-index: 2;
    font-family: "Marcellus SC", serif; font-size: 25px; color: var(--bullet); line-height: 33px;
  }
  .benefits li::before { content: "\25C6"; font-size: 15px; margin-right: 10px; vertical-align: 3px; }

  .brand { display: flex; align-items: center; gap: 8px; font-family: "Marcellus", serif; color: var(--navy); }
  .brand .mark { background: var(--brand-green); display: block; }
  .wall-brand { position: absolute; left: 430px; top: 540px; font-size: 26px; z-index: 2; }
  .wall-brand .mark { width: 30px; height: 30px; }

  .podium {
    position: absolute; left: 420px; top: 700px; width: 360px; height: 270px;
    background: linear-gradient(to bottom, var(--white) 60%, var(--water) 100%);
    overflow: hidden;
  }
  .podium .swoosh { position: absolute; left: 0; top: 0; width: 360px; height: 140px; }
  .podium-book { left: 22px; top: 18px; width: 130px; height: 220px; z-index: 2; }
  .podium-book .title { top: 30px; font-size: 25px; }
  .podium-book .subtitle { top: 172px; padding: 3px 2px; font-size: 8px; }
  .podium-book .author { top: 200px; font-size: 9px; letter-spacing: 2px; }
  .podium-heading {
    position: absolute; left: 170px; width: 180px; top: 58px; text-align: center;
    font-family: "Marcellus", serif; font-weight: 400;
    font-size: 19px; line-height: 26px; color: var(--ink); z-index: 2;
  }
  .podium-brand { position: absolute; left: 186px; top: 178px; font-size: 13px; z-index: 2; }
  .podium-brand .mark { width: 14px; height: 14px; }
</style>
</head>
<body>

<section class="back-wall">
  <div class="side-band left"></div>
  <div class="side-band right"></div>
  <svg class="swoosh" viewBox="0 0 1080 300" preserveAspectRatio="none" aria-hidden="true">
    <path d="M0 0 H1080 V190 C880 150 700 200 520 250 C360 290 230 240 0 170 Z" fill="var(--sky)"/>
    <path d="M0 140 C200 220 360 270 520 230 C700 180 860 170 1080 210 V240 C880 205 720 215 540 265 C360 310 190 250 0 175 Z" fill="var(--navy)"/>
    <path d="M560 255 C720 210 900 200 1080 225 V232 C900 212 740 222 560 262 Z" fill="var(--white)"/>
  </svg>
  <h1 class="wall-heading">Join Our Strategic Alliance Program</h1>

  <div class="book wall-book">
    <div class="portrait" role="img" aria-label="Author portrait in suit and tie"></div>
    <div class="cover-glow"></div>
    <div class="title"><span class="w">Don't</span><span class="w">Say I</span><span class="w">Never</span><span class="b">Warned</span><span class="b">You</span></div>
    <div class="subtitle">The Only Wealth Guide<br>You'll Ever Need</div>
    <div class="author">Ned Calloway</div>
  </div>

  <ul class="benefits">
    <li>Offer financial planning services</li>
    <li>Increase client retention</li>
    <li>Strengthen client relationships</li>
    <li>Increase client referrals</li>
    <li>Enhance your reputation</li>
    <li>Earn ongoing revenue</li>
  </ul>

  <div class="brand wall-brand"><span class="mark"></span><span>Wrenfield Capital</span></div>
</section>

<section class="podium">
  <svg class="swoosh" viewBox="0 0 360 140" preserveAspectRatio="none" aria-hidden="true">
    <path d="M140 60 C220 35 290 30 360 35 V46 C290 42 220 48 140 72 Z" fill="var(--navy)"/>
  </svg>
  <div class="book podium-book">
    <div class="portrait" role="img" aria-label="Author portrait in suit and tie"></div>
    <div class="cover-glow"></div>
    <div class="title"><span class="w">Don't</span><span class="w">Say I</span><span class="w">Never</span><span class="b">Warned</span><span class="b">You</span></div>
    <div class="subtitle">The Only Wealth Guide<br>You'll Ever Need</div>
    <div class="author">Ned Calloway</div>
  </div>
  <h2 class="podium-heading">Join Our<br>Strategic<br>Alliance<br>Program</h2>
  <div class="brand podium-brand"><span class="mark"></span><span>Wrenfield Capital</span></div>
</section>

</body>
</html>
```